Website Design for Business Law Firm

We have a logo and now we would like a web site design for our new website. Our small firm provides creative and aggressive transactional (not litigation) legal services to advise healthcare, technology, internet-based and traditional companies and investors in such companies on healthcare, technology, financing, mergers/acquisitions, real estate and other transactions, legal compliance and general corporate and business matters.

We would like to see a website design that is professional and appropriate for executives, professionals, investors and government regulators to visit, that conveys professionalism and competence while being a little edgy and modern - no typical legal motifs such as gavels, books, or scales of justice. We advise businesses and investors and guide them through complicated issues quickly, capably and differently from other law firms. We are part of the business team and get things done.

The logo is attached, and we like gray as a color to complement it. The intention of the logo is to convey that in a storm or challenging time, people come to this firm, and people come to this firm when they need the power and disruption to change things or shake them up.

I have also enclosed a picture of our business card for consideration.

On the other hand, you can check out the current simple site at www.quenlow.example to see we have used a space motif in the past to evoke that we help create stars (the nebula featured there). This is not a necessary part of the new website and it may look better without it.

We appreciate your creativity and look forward to designs.

Industry/Entity Type

Business

Requirements
Must have
• We anticipate the following pages, and you may submit different ideas for the different pages:
• 1. Landing page
• 2. Services pages - healthcare, IT/Technology, general counsel services, financings, mergers/acquisitions, mediation/arbitration, procurement and productization
• 3. About Us including contact information
• Our name and contact information:
• Quenlow Law Firm, P.C.
• 7816 SW 19th Ave.
• Portland, OR 97213
• phone: 555.614.2873
• fax: 555.730.4158
Nice to have
• Please consider designs that enhance the impressions we are looking for
Should not have
• Please no gavels, scales of justice, law books, or similar traditional legal imagery.

```html
<!DOCTYPE html>
<html lang="en">
<head>
<meta charset="utf-8">
<title>Quenlow Law Firm, P.C.</title>
<link rel="stylesheet" href="https://fonts.googleapis.com/css2?family=Yanone+Kaffeesatz:wght@400;500&family=Open+Sans:wght@700&display=swap">
<style>
  :root {
    --blue: #1ba3d6;
    --ink: #1d1d1f;
    --white: #ffffff;
    --footer: #25282c;
    --footer-text: #cfd2d6;
    --hero-dark: #050607;
    --hero-mid: #2d3c42;
    --hero-light: #7f9aa3;
  }
  * { margin: 0; padding: 0; box-sizing: border-box; }
  html, body { width: 1200px; height: 813px; overflow: hidden; background: var(--white); }
  .page { position: relative; width: 1200px; height: 813px; font-family: Arial, Helvetica, sans-serif; color: var(--ink); }

  .site-header { position: absolute; left: 0; top: 0; width: 1200px; height: 145px; }
  .brand {
    position: absolute; left: 175px; top: 24px; width: 365px; height: 88px;
    display: flex; align-items: center; gap: 14px;
    font-family: "Yanone Kaffeesatz", sans-serif; font-weight: 400;
    font-size: 64px; letter-spacing: 10px; color: var(--ink);
  }
  .brand-mark { width: 30px; height: 30px; background: var(--ink); flex: none; }
  .header-fax {
    position: absolute; right: 210px; top: 45px;
    font-family: "Yanone Kaffeesatz", sans-serif; font-weight: 500; font-size: 21px; color: var(--ink);
  }
  .main-nav {
    position: absolute; right: 205px; top: 80px; display: flex; gap: 20px;
    font-family: "Yanone Kaffeesatz", sans-serif; font-weight: 400; font-size: 20px;
  }
  .main-nav a { color: var(--blue); text-decoration: none; }

  .hero { position: absolute; left: 0; top: 145px; width: 1200px; height: 285px; overflow: hidden; }
  .hero-visual {
    position: absolute; inset: 0;
    background:
      radial-gradient(ellipse 260px 200px at 190px 20px, var(--hero-light), transparent 70%),
      linear-gradient(90deg, var(--hero-mid) 0%, #1c2529 45%, #0f1416 75%, var(--hero-dark) 100%);
  }
  .hero-copy { position: absolute; left: 0; top: 0; width: 1248px; text-align: center; font-family: "Open Sans", sans-serif; font-weight: 700; color: var(--white); text-shadow: 0 2px 3px rgba(0,0,0,.9); }
  .hero-lead { position: absolute; left: 0; width: 100%; top: 62px; font-size: 27px; }
  .hero-title { position: absolute; left: 0; width: 100%; top: 101px; font-size: 37px; letter-spacing: 0.5px; }
  .hero-button {
    position: absolute; left: 545px; top: 168px; width: 178px; height: 60px;
    background: var(--blue); border: 2px solid var(--white); border-radius: 6px;
    display: flex; align-items: center; justify-content: center;
    font-family: "Yanone Kaffeesatz", sans-serif; font-size: 29px; color: var(--white); text-decoration: none;
  }

  .features { position: absolute; top: 476px; left: 0; width: 1200px; }
  .feature { position: absolute; width: 272px; }
  .feature:nth-child(1) { left: 173px; }
  .feature:nth-child(2) { left: 466px; }
  .feature:nth-child(3) { left: 753px; }
  .feature h2 { font-family: "Yanone Kaffeesatz", sans-serif; font-weight: 400; font-size: 27px; line-height: 34px; color: var(--ink); }
  .feature p { margin-top: 6px; font-size: 12px; line-height: 18.6px; color: #111; }

  .contact { position: absolute; top: 618px; left: 0; width: 1200px; font-family: "Yanone Kaffeesatz", sans-serif; font-size: 28px; line-height: 30.4px; color: var(--blue); font-style: normal; }
  .contact-block { position: absolute; }
  .contact-block.address { left: 323px; }
  .contact-block.reach { left: 635px; }

  .site-footer {
    position: absolute; left: 0; top: 782px; width: 1200px; height: 31px;
    background: var(--footer); border-top: 1px solid #0d0e10;
    display: flex; align-items: center; justify-content: center;
    font-size: 10.5px; color: var(--footer-text);
  }
  .site-footer a { color: var(--footer-text); text-decoration: none; }
</style>
</head>
<body>
<div class="page">
  <header class="site-header">
    <div class="brand"><span class="brand-mark"></span>QUENLOW</div>
    <div class="header-fax">FAX: 555.730.4158</div>
    <nav class="main-nav">
      <a href="#">REAL ESTATE</a>
      <a href="#">CONTRACTS</a>
      <a href="#">OUTSOURCING</a>
      <a href="#">PROCUREMENTS</a>
    </nav>
  </header>

  <section class="hero">
    <div class="hero-visual" role="img" aria-label="Dark stormy sky crossed by bright lightning bolts"></div>
    <div class="hero-copy">
      <p class="hero-lead">Pragmatic, Creative Services for</p>
      <h1 class="hero-title">INNOVATIVE BUSINESSES</h1>
    </div>
    <a class="hero-button" href="#">LEARN MORE</a>
  </section>

  <section class="features">
    <article class="feature">
      <h2>Strategic Alliances</h2>
      <p>Lorem ipsum dolor sit amet, consectetuer adipisc-ing elit, sed diam nonummy nibh euismod tincidunt ut laoreet dolore magna aliquam erat volutpat. Ut wisi enim</p>
    </article>
    <article class="feature">
      <h2>Business Relationships</h2>
      <p>Lorem ipsum dolor sit amet, consectetuer adipisc-ing elit, sed diam nonummy nibh euismod tincidunt ut laoreet dolore magna aliquam erat volutpat. Ut</p>
    </article>
    <article class="feature">
      <h2>Outsourcing</h2>
      <p>Lorem ipsum dolor sit amet, consectetuer adipisc-ing elit, sed diam nonummy nibh euismod tincidunt ut laoreet dolore magna aliquam erat volutpat. Ut</p>
    </article>
  </section>

  <address class="contact">
    <div class="contact-block address">Quenlow Law Firm, P.C.<br>P.O. Box 6125<br>Portland, OR 97213</div>
    <div class="contact-block reach">info@quenlow.example<br>phone 555.614.2873<br>fax 555.730.4196</div>
  </address>

  <footer class="site-footer">
    Copyright 2013 Quenlow Law Firm - <a href="#">&nbsp;Terms &amp; Conditions</a>&nbsp;|&nbsp;<a href="#">Privacy Policy</a>
  </footer>
</div>
</body>
</html>
```